Create a intrest card to get people contact info

Hello,

I would like to create an updated "survey slip". It is simply a card people can fill out if they are interested and programs and would like be contacted. For ease of printing I want to try to fit 3 or 4 per page.

They info we would need would be as follows:

Name
School
Break Time
Email
Phone Number

And then boxes to check for:

What programs are you interested in hearing more about
Disability
Cancer
Heart and Stroke
Accident
Term Life Insurance

Best form of contact (then boxes to check with spaces)
Phone call
Text
Email
In person meeting

```html
<!DOCTYPE html>
<html lang="en">
<head>
<meta charset="utf-8">
<title>Interest Card</title>
<link rel="stylesheet" href="https://fonts.googleapis.com/css2?family=Francois+One&family=Archivo+Narrow:wght@400;500&display=swap">
<style>
  :root {
    --paper: #ffffff;
    --ink: #111111;
    --line: #1a1a1a;
    --panel-fill: #dcedf3;
    --panel-edge: #263646;
  }
  * { box-sizing: border-box; margin: 0; padding: 0; }
  html, body {
    width: 851px;
    height: 1200px;
    overflow: hidden;
    background: var(--paper);
  }
  .interest-card {
    position: relative;
    width: 851px;
    height: 1200px;
    background: var(--paper);
    color: var(--ink);
    font-family: "Archivo Narrow", "Arial Narrow", sans-serif;
  }
  .card-frame {
    position: absolute;
    left: 11px; top: 11px;
    width: 828px; height: 1178px;
    border: 3px solid var(--line);
    border-radius: 80px;
  }
  .section-title {
    position: absolute;
    left: 0; width: 851px;
    text-align: center;
    white-space: nowrap;
    font-family: "Francois One", "Arial Narrow", sans-serif;
    font-size: 38px;
    line-height: 1;
    letter-spacing: 0.5px;
  }
  .section-title--personal { top: 64px; }
  .section-title--programs { top: 538px; font-size: 31px; letter-spacing: 0; }
  .section-title--contact { top: 968px; }

  .field {
    position: absolute;
    left: 89px;
    width: 690px;
    height: 46px;
  }
  .field-label {
    position: absolute;
    left: 0; top: 6px;
    font-size: 29px;
    font-weight: 500;
    line-height: 1;
  }
  .field-colon {
    position: absolute;
    left: 285px; top: 4px;
    font-size: 30px;
    font-weight: 500;
    line-height: 1;
  }
  .field-input {
    position: absolute;
    left: 302px; top: 0;
    width: 380px; height: 46px;
    border: 2.5px solid var(--line);
    border-radius: 8px;
  }
  .field--name   { top: 132px; }
  .field--school { top: 197px; }
  .field--break  { top: 264px; }
  .field--email  { top: 328px; }
  .field--phone  { top: 400px; }

  .program-panel {
    position: absolute;
    left: 140px; top: 590px;
    width: 546px; height: 334px;
    background: var(--panel-fill);
    border: 3px solid var(--panel-edge);
    border-radius: 70px;
  }
  .check-option {
    position: absolute;
    display: flex;
    align-items: center;
    gap: 28px;
    font-size: 29px;
    font-weight: 500;
    line-height: 1;
    white-space: nowrap;
  }
  .check-box {
    width: 54px; height: 46px;
    border: 2.5px solid var(--line);
    border-radius: 9px;
    background: var(--paper);
    flex: none;
  }
  .program-panel .check-box { background: transparent; }
  .program-panel .check-option { left: 86px; }
  .program--disability { top: 16px; }
  .program--cancer     { top: 80px; }
  .program--heart      { top: 146px; }
  .program--accident   { top: 210px; }
  .program--term-life  { top: 274px; }

  .contact-option .check-box { width: 56px; height: 46px; }
  .contact-option { gap: 20px; }
  .contact--call   { left: 112px; top: 1026px; }
  .contact--text   { left: 112px; top: 1093px; }
  .contact--email  { left: 438px; top: 1026px; }
  .contact--meet   { left: 438px; top: 1093px; }
</style>
</head>
<body>
<main class="interest-card">
  <div class="card-frame"></div>

  <h2 class="section-title section-title--personal">Personal Information</h2>

  <div class="field field--name"><span class="field-label">Name</span><span class="field-colon">:</span><span class="field-input"></span></div>
  <div class="field field--school"><span class="field-label">School</span><span class="field-colon">:</span><span class="field-input"></span></div>
  <div class="field field--break"><span class="field-label">Break Time :</span><span class="field-input"></span></div>
  <div class="field field--email"><span class="field-label">Email</span><span class="field-colon">:</span><span class="field-input"></span></div>
  <div class="field field--phone"><span class="field-label">Phone Number</span><span class="field-colon">:</span><span class="field-input"></span></div>

  <h2 class="section-title section-title--programs">What programs are you interested in hearing more about?</h2>

  <div class="program-panel">
    <div class="check-option program--disability"><span class="check-box"></span>Disability</div>
    <div class="check-option program--cancer"><span class="check-box"></span>Cancer</div>
    <div class="check-option program--heart"><span class="check-box"></span>Heart and Stroke</div>
    <div class="check-option program--accident"><span class="check-box"></span>Accident</div>
    <div class="check-option program--term-life"><span class="check-box"></span>Term Life Insurance</div>
  </div>

  <h2 class="section-title section-title--contact">Best form of contact</h2>

  <div class="check-option contact-option contact--call"><span class="check-box"></span>Phone call</div>
  <div class="check-option contact-option contact--text"><span class="check-box"></span>Text</div>
  <div class="check-option contact-option contact--email"><span class="check-box"></span>Email</div>
  <div class="check-option contact-option contact--meet"><span class="check-box"></span>In person meeting</div>
</main>
</body>
</html>
```